HVAC Contractor Website Design

We are working with an HVAC contractor in Idaho called QR HVAC.
Some sites to use for content/competitors and inspiration:
https://www.brindlevent.example
https://plumcrest.example/web/contractor/ (lots of contractor website designs we've approved and continue to show clients)
Thank you for taking the time to consider designing a website for us. We are web developers based in Stockton, CA, USA. Most of our projects go through the same process. Understanding this process may help you win a project with us. We custom-code all of our websites in-house. We don’t have any requirements as to what tools you use for your design, but we prefer Figma files. For any design that we label as four-stars, we send it to the client for review. The client picks the final design they want us to use. Once we complete this process, we will continue to show additional clients all the four-star sites and purchase them later. Your designs will have multiple chances to sell. For better chances of success, we ask that you follow these guidelines.
IMAGES:
If you use any images or icons in the design, we ask that you have a link to the asset so we can purchase the image/icon. Most of the designs we submit do not have the customer’s images on them unless they have some great images. Be creative; show us the feeling you are trying to portray with your image choices. Use any royalty-free site you choose. We subscribe to Velmora and mainly use their images, but we can purchase images outside of Velmora.
PLEASE NOTE: we will not submit designs to clients with watermarks on the images.
FONTS:
We ask that you identify the fonts used in the design. This can be done in a message if you want. We typically use Google Fonts and Velmora Fonts.
CONTENT:
We're always open to different content and ideas. We often submit designs with stock images so the client can see our vision. We typically take pictures after the website launch to use their images with our vision. Lorem Ipsum is fine for paragraphs, but we ask that you write the headers in correct English. We want to be able to show the vision and identify the sections of the website.
INSPIRATION:
We typically add a couple of links in the brief of websites we like to help you get started in your design.
REVISIONS:
We do not often ask for revisions of the designs unless we see something in the design that may not appeal to the client. If there are slight changes that we want to make, we do that in the development process.
FEEDBACK:
We rarely give feedback on designs during the design process. We are working on many website projects and do not have the time to provide feedback. We usually respond if your request is well thought out and asks specific questions, but a note asking “feedback, please” usually goes unanswered
Number of Pages Required
1 page
Look and feel
Each slider illustrates characteristics of the customer's brand and the style your logo design should communicate.

```html
<!DOCTYPE html>
<html lang="en">
<head>
<meta charset="utf-8">
<title>QR HVAC – Heating and Air Conditioning Services</title>
<link href="https://fonts.googleapis.com/css2?family=Montserrat:wght@400;500;600;700;800&display=swap" rel="stylesheet">
<style>
:root{
  --red:#e3262b;
  --orange:#ff4d12;
  --blue:#1c5fb6;
  --blue-light:#2a8fe2;
  --navy:#0c1a3c;
  --band:#1f4d91;
  --ink:#1b1b1b;
  --muted:#5b5b5b;
  --line:#e6e6e6;
  --field:#f1f1f1;
  --white:#fff;
}
*{box-sizing:border-box;margin:0;padding:0}
html,body{width:1200px;height:4428px;overflow:hidden}
body{position:relative;font-family:'Montserrat',sans-serif;color:var(--ink);background:var(--white)}
.abs{position:absolute}
a{color:inherit;text-decoration:none}

/* top bar */
.topbar{left:0;top:0;width:1200px;height:41px;background:linear-gradient(90deg,var(--blue),var(--blue-light));color:var(--white);font-size:16px;display:flex;align-items:center;padding:0 50px}
.topbar .item{display:flex;align-items:center;gap:8px;margin-right:58px}
.topbar .socials{margin-left:auto;display:flex;gap:12px}
.topbar .socials span{width:16px;height:16px;border-radius:50%;background:var(--white);opacity:.9}

/* nav */
.nav{left:0;top:41px;width:1200px;height:100px;display:flex;align-items:center;font-weight:600;font-size:18px;letter-spacing:.3px}
.nav a{position:absolute;top:44px}
.nav a.active{color:var(--red)}
.brand{position:absolute;left:450px;top:0;width:280px;height:100px;display:flex;align-items:center;justify-content:center;gap:10px;font-size:30px;font-weight:700;color:var(--ink);letter-spacing:1px}
.brand i{width:14px;height:14px;background:var(--red);display:block}

/* hero */
.hero{left:0;top:141px;width:1200px;height:720px;overflow:hidden}
.hero .photo{position:absolute;inset:0;background:linear-gradient(180deg,#3a4453 0%,#5d5a55 55%,#3d3a36 100%)}
.hero .shade{position:absolute;inset:0;background:rgba(10,18,32,.45)}
.hero h1{position:absolute;left:0;width:1200px;top:130px;text-align:center;color:var(--white);font-size:52px;font-weight:700;line-height:64px;text-transform:uppercase}
.hero p{position:absolute;left:0;width:1200px;top:268px;text-align:center;color:var(--white);font-size:23px;line-height:28px}
.btn{display:inline-flex;align-items:center;justify-content:center;background:var(--red);color:var(--white);font-weight:600;text-transform:uppercase}
.hero .btn{position:absolute;left:490px;top:370px;width:210px;height:48px;font-size:20px}

/* feature cards */
.feature{width:260px;height:222px;background:var(--white);border-radius:12px;box-shadow:0 4px 18px rgba(0,0,0,.12);text-align:center;padding-top:16px}
.feature h3{font-size:17px;font-weight:600;margin-top:6px}
.feature p{font-size:9px;color:var(--muted);line-height:16px;margin-top:12px;text-transform:uppercase}
.feature .more{display:inline-flex;align-items:center;gap:8px;margin-top:16px;color:var(--red);font-size:12px;font-weight:700}

/* about blocks */
.photo-block{background:linear-gradient(135deg,#8a7a5c,#c9b592 55%,#e9e4da)}
.photo-block.blue{background:linear-gradient(135deg,#6f7f93,#b8c4d0 50%,#dfe4ea)}
.photo-block.tech{background:linear-gradient(135deg,#eceae6,#a0876a 45%,#2a4f9a)}
.text-box{background:var(--white);box-shadow:0 2px 14px rgba(0,0,0,.06);padding:44px 50px 0}
.text-box h2{font-size:29px;font-weight:600;letter-spacing:.5px}
.text-box p{font-size:13.5px;line-height:20px;color:var(--muted);margin-top:18px;width:450px}
.text-box .btn{height:42px;padding:0 40px;font-size:15px;margin-top:40px}

/* services */
.services{left:0;top:1992px;width:1200px;height:690px;background:linear-gradient(180deg,rgba(31,77,145,.95),rgba(28,70,140,.92)),var(--band)}
.section-title{font-size:29px;font-weight:600;text-align:center;width:1200px;left:0}
.services .section-title{color:var(--white);top:60px}
.svc{top:164px;width:270px;height:364px;background:var(--white);border-radius:12px;padding:12px 16px}
.svc .img{height:146px;border-radius:4px}
.svc .icon{width:64px;height:64px;border-radius:50%;background:var(--red);margin:-32px 0 0 28px;position:relative;display:flex;align-items:center;justify-content:center;border:3px solid var(--white)}
.svc h3{font-size:15px;font-weight:700;margin-top:10px}
.svc p{font-size:10.5px;line-height:13px;color:var(--muted);margin-top:6px}
.svc .more{display:flex;align-items:center;gap:6px;color:var(--red);font-size:9.5px;font-weight:600;margin-top:18px}
.svc .more b{width:12px;height:12px;border-radius:50%;background:var(--red)}
.services .btn{position:absolute;left:500px;top:588px;width:219px;height:46px;font-size:14px;font-weight:500}

/* testimonials */
.quote{top:2902px;width:483px;height:206px;background:var(--white);border-radius:12px;box-shadow:0 4px 20px rgba(0,0,0,.08);padding:22px 56px}
.quote .head{display:flex;align-items:center;gap:20px}
.quote .avatar{width:62px;height:62px;border-radius:50%;background:linear-gradient(135deg,#c9d3de,#5d6f84)}
.quote h4{font-size:17px;font-weight:600}
.quote .stars{display:flex;gap:6px;margin-top:8px}
.quote p{font-size:11.5px;line-height:14px;color:var(--muted);margin-top:34px}
.quote .rule{height:2px;background:#f4a0a2;margin-top:20px;width:385px}
.dots{top:3164px;left:540px;display:flex;gap:14px}
.dots span{width:24px;height:24px;border-radius:50%;background:var(--red)}
.dots span.off{background:var(--white);border:2px solid var(--red)}

/* contact */
.form-box{left:110px;top:3493px;width:567px;height:397px;background:var(--white);box-shadow:0 2px 16px rgba(0,0,0,.06);padding:36px 47px 0}
.form-box h2{font-size:31px;font-weight:600;text-align:center}
.fields{display:grid;grid-template-columns:228px 228px;gap:16px 18px;margin-top:30px}
.field{height:36px;background:var(--field);border:1px solid #e4e4e4;border-radius:3px;font-size:15px;padding:9px 12px;color:#333}
.field.wide{grid-column:1/3;height:120px}
.form-box .btn{margin:28px 0 0 64px;width:350px;height:44px;font-size:13px;font-weight:500;border-radius:3px}

/* footer */
.footer{left:0;top:3954px;width:1200px;height:474px;background:var(--navy);color:var(--white)}
.col{top:68px}
.col h5{font-size:18px;font-weight:700}
.col .under{width:52px;height:3px;background:var(--blue);margin-top:16px}
.col p{font-size:14px;line-height:28px;margin-top:26px;width:265px}
.round{display:flex;gap:14px;margin-top:22px}
.round span{width:42px;height:42px;border-radius:50%;background:var(--blue)}
.info-row{display:flex;gap:24px;margin-top:18px;font-size:14px;line-height:24px}
.info-row svg{flex:none;margin-top:6px}
.info-row b{font-weight:700}
.links{margin-top:20px;width:270px}
.links div{display:flex;justify-content:space-between;font-size:13.5px;padding:13px 0;border-bottom:1px solid rgba(255,255,255,.15)}
</style>
</head>
<body>

<div class="abs topbar">
  <div class="item">
    <svg width="22" height="22" viewBox="0 0 22 22"><circle cx="11" cy="11" r="10" fill="none" stroke="#fff" stroke-width="1.6"/><rect x="6" y="7.5" width="10" height="7" fill="none" stroke="#fff" stroke-width="1.3"/><path d="M6 7.5l5 4 5-4" fill="none" stroke="#fff" stroke-width="1.3"/></svg>
    info@qrhvac.example
  </div>
  <div class="item">
    <svg width="22" height="22" viewBox="0 0 22 22"><circle cx="11" cy="11" r="10" fill="none" stroke="#fff" stroke-width="1.6"/><path d="M8 6c-1 1-1 3 1 6s4 4 5 3l1-1-2-2-1 1c-1 0-3-2-3-3l1-1-2-3z" fill="#fff"/></svg>
    (555) 014 7821
  </div>
  <div class="socials"><span></span><span></span><span></span></div>
</div>

<nav class="abs nav">
  <a class="active" style="left:58px">HOME</a>
  <a style="left:176px">ABOUT</a>
  <a style="left:306px">SERVICES</a>
  <div class="brand"><i></i>QR HVAC</div>
  <a style="left:762px">TESTIMONIALS</a>
  <a style="left:962px">BLOG</a>
  <a style="left:1074px">CONTACT</a>
</nav>

<section class="abs hero">
  <div class="photo" role="img" aria-label="Photo of a domed state capitol building at dusk"></div>
  <div class="shade"></div>
  <svg class="abs" style="left:0;top:0" width="1200" height="720" viewBox="0 0 1200 720">
    <polygon points="0,660 1200,520 1200,585 0,672" fill="var(--orange)"/>
    <polygon points="0,672 1200,585 1200,720 0,720" fill="#f5f5f5"/>
  </svg>
  <h1>Heating and Air<br>Conditioning Services</h1>
  <p>Lorem ipsum dolor sit amet, consectetuer adipiscing elit.<br>Aenean commodo ligula eget dolor.<br>Aenean massa.</p>
  <a class="btn">Get a Quote</a>
</section>

<div class="abs feature" style="left:136px;top:660px">
  <svg width="66" height="72" viewBox="0 0 66 72"><g fill="none" stroke="var(--red)" stroke-width="3.5" stroke-linecap="round"><path d="M16 4c-5 6 5 10 0 18s5 10 0 18"/><path d="M33 4c-5 6 5 10 0 18s5 10 0 18"/><path d="M50 4c-5 6 5 10 0 18s5 10 0 18"/><path d="M4 50h58M4 59h58M4 68h58"/></g></svg>
  <h3>Heating</h3>
  <p>Lorem ipsum dolor sit amet,<br>consectetuer adipiscing elit.</p>
  <a class="more">READ MORE <svg width="22" height="10" viewBox="0 0 22 10"><path d="M0 5h18M14 1l5 4-5 4" stroke="var(--red)" stroke-width="2.2" fill="none"/></svg></a>
</div>
<div class="abs feature" style="left:474px;top:660px">
  <svg width="66" height="72" viewBox="0 0 66 72"><g stroke="var(--red)" stroke-width="4" stroke-linecap="round" fill="none"><path d="M33 6v60M7 21l52 30M7 51l52-30"/><path d="M25 10l8 8 8-8M25 62l8-8 8 8M9 31l11-3-3-11M57 41l-11 3 3 11M9 41l11 3-3 11M57 31l-11-3 3-11"/></g></svg>
  <h3>Cooling</h3>
  <p>Lorem ipsum dolor sit amet,<br>consectetuer adipiscing elit.</p>
  <a class="more">READ MORE <svg width="22" height="10" viewBox="0 0 22 10"><path d="M0 5h18M14 1l5 4-5 4" stroke="var(--red)" stroke-width="2.2" fill="none"/></svg></a>
</div>
<div class="abs feature" style="left:818px;top:660px">
  <svg width="72" height="72" viewBox="0 0 72 72"><g stroke="var(--red)" stroke-width="4" stroke-linecap="round" stroke-linejoin="round" fill="none"><path d="M12 60l28-28c-4-8 2-18 12-18l-7 7 2 6 6 2 7-7c0 10-10 16-18 12L14 62z"/><path d="M10 10l6-2 18 18-4 4L12 12z"/><path d="M42 46l14 14 4-4-14-14"/></g></svg>
  <h3>Repairs</h3>
  <p>Lorem ipsum dolor sit amet,<br>consectetuer adipiscing elit.</p>
  <a class="more">READ MORE <svg width="22" height="10" viewBox="0 0 22 10"><path d="M0 5h18M14 1l5 4-5 4" stroke="var(--red)" stroke-width="2.2" fill="none"/></svg></a>
</div>

<div class="abs photo-block" style="left:70px;top:964px;width:496px;height:366px" role="img" aria-label="Photo of a technician in a cap working on a wall unit"></div>
<div class="abs text-box" style="left:502px;top:1059px;width:569px;height:354px">
  <h2>WHO WE ARE</h2>
  <p>Many business owners struggle to understand and maximize the true value of their businesses. This lack of awareness can lead to selling their business for less than it's worth, poor timing in the market, and inadequate preparation for the complexities of a business sale. They often face challenges in making their business attractive to buyers and aligning the sale with their personal and financial goals. This overall lack of preparedness and insight can result in significant financial and emotional regrets post-sale.</p>
  <a class="btn">More About Us</a>
</div>

<div class="abs photo-block blue" style="left:578px;top:1525px;width:493px;height:366px" role="img" aria-label="Photo of two technicians inspecting a ceiling air duct"></div>
<div class="abs text-box" style="left:70px;top:1597px;width:570px;height:354px">
  <h2>WHAT WE DO</h2>
  <p>Many business owners struggle to understand and maximize the true value of their businesses. This lack of awareness can lead to selling their business for less than it's worth, poor timing in the market, and inadequate preparation for the complexities of a business sale. They often face challenges in making their business attractive to buyers and aligning the sale with their personal and financial goals. This overall lack of preparedness and insight can result in significant financial and emotional regrets post-sale.</p>
  <a class="btn">Contact Us Now</a>
</div>

<section class="abs services">
  <h2 class="abs section-title">OUR SERVICES</h2>
  <div class="abs svc" style="left:119px">
    <div class="img" style="background:linear-gradient(135deg,#7b8794,#c9c4bd 50%,#b23a3a)" role="img" aria-label="Photo of a fitter tightening a gas pipe"></div>
    <div class="icon"><svg width="30" height="30" viewBox="0 0 30 30" fill="none" stroke="#fff" stroke-width="2"><rect x="7" y="5" width="16" height="20" rx="2"/><path d="M7 11h16M12 17l-2 2 2 2M18 17l2 2-2 2"/></svg></div>
    <h3>GAS FITTING</h3>
    <p>Lorem ipsum dolor sit amet, consectetuer adipiscing elit. Aenean commodo ligula eget dolor. Aenean massa. Cum sociis natoque penatibus et magnis dis parturient montes, nascetur ridiculus mus.</p>
    <a class="more">READ MORE <b></b></a>
  </div>
  <div class="abs svc" style="left:466px">
    <div class="img" style="background:linear-gradient(135deg,#6b5a48,#c49a76 50%,#e7ddd0)" role="img" aria-label="Photo of a plumber fitting pipes"></div>
    <div class="icon"><svg width="30" height="30" viewBox="0 0 30 30" fill="none" stroke="#fff" stroke-width="2"><rect x="5" y="6" width="20" height="18" rx="2"/><circle cx="15" cy="16" r="4"/><path d="M5 11h20"/></svg></div>
    <h3>PIPE FITTING</h3>
    <p>Lorem ipsum dolor sit amet, consectetuer adipiscing elit. Aenean commodo ligula eget dolor. Aenean massa. Cum sociis natoque penatibus et magnis dis parturient montes, nascetur ridiculus mus.</p>
    <a class="more">READ MORE <b></b></a>
  </div>
  <div class="abs svc" style="left:813px">
    <div class="img" style="background:linear-gradient(135deg,#3b4350,#8e959c 55%,#d8dadc)" role="img" aria-label="Photo of a technician installing an outdoor AC unit"></div>
    <div class="icon"><svg width="30" height="30" viewBox="0 0 30 30" fill="none" stroke="#fff" stroke-width="2"><rect x="5" y="7" width="20" height="16" rx="2"/><circle cx="15" cy="15" r="5"/><path d="M15 10v10M10 15h10"/></svg></div>
    <h3>NEW INSTALLS</h3>
    <p>Lorem ipsum dolor sit amet, consectetuer adipiscing elit. Aenean commodo ligula eget dolor. Aenean massa. Cum sociis natoque penatibus et magnis dis parturient montes, nascetur ridiculus mus.</p>
    <a class="more">READ MORE <b></b></a>
  </div>
  <a class="btn">View All Services</a>
</section>

<h2 class="abs section-title" style="top:2778px">WHAT CLIENT SAYS</h2>
<div class="abs quote" style="left:67px">
  <div class="head">
    <div class="avatar" role="img" aria-label="Client portrait"></div>
    <div><h4>Mara Ellison</h4>
      <div class="stars"><svg width="110" height="18" viewBox="0 0 110 18" fill="var(--red)"><path id="st" d="M9 0l2.6 6 6.4.5-4.9 4.2 1.5 6.3L9 13.6 3.4 17l1.5-6.3L0 6.5 6.4 6z"/><use href="#st" x="23"/><use href="#st" x="46"/><use href="#st" x="69"/><use href="#st" x="92"/></svg></div>
    </div>
  </div>
  <p>Lorem ipsum dolor sit amet, consectetur adipiscing elit, sed do eiusmod tempor incididunt ut labore et dolore magna aliqua. Ut enim ad minim veniam, quis nostrud exercitation ullamco laboris nisi ut aliquip ex ea commodo consequat.</p>
  <div class="rule"></div>
</div>
<div class="abs quote" style="left:629px;padding-top:30px">
  <div class="head">
    <div class="avatar" style="background:linear-gradient(135deg,#e6d3c6,#8a5a43)" role="img" aria-label="Client portrait"></div>
    <div><h4>Mara Ellison</h4>
      <div class="stars"><svg width="110" height="18" viewBox="0 0 110 18" fill="var(--red)"><use href="#st"/><use href="#st" x="23"/><use href="#st" x="46"/><use href="#st" x="69"/><use href="#st" x="92"/></svg></div>
    </div>
  </div>
  <p>Lorem ipsum dolor sit amet, consectetur adipiscing elit, sed do eiusmod tempor incididunt ut labore et dolore magna aliqua. Ut enim ad minim veniam, quis nostrud exercitation ullamco laboris nisi ut aliquip ex ea commodo consequat.</p>
  <div class="rule"></div>
</div>
<div class="abs dots"><span></span><span class="off"></span><span></span></div>

<div class="abs photo-block tech" style="left:615px;top:3459px;width:494px;height:366px" role="img" aria-label="Photo of a technician in a blue cap servicing a boiler"></div>
<div class="abs form-box">
  <h2>CONTACT US NOW</h2>
  <div class="fields">
    <div class="field">Name</div><div class="field">Email</div>
    <div class="field">Phone</div><div class="field">Service</div>
    <div class="field wide">Message</div>
  </div>
  <a class="btn">Request a Quote Now</a>
</div>

<footer class="abs footer">
  <div class="abs col" style="left:27px">
    <h5>ABOUT US</h5><div class="under"></div>
    <p>We are an award winning plumbing company with over 20 years experience in the business. We provide a wide range of services for both residential and commercial clients.</p>
    <div class="round"><span></span><span></span><span></span></div>
  </div>
  <div class="abs col" style="left:341px">
    <h5>CONTACT US</h5><div class="under"></div>
    <div style="margin-top:14px">
      <div class="info-row"><svg width="18" height="24" viewBox="0 0 18 24"><path d="M9 1a8 8 0 0 0-8 8c0 6 8 14 8 14s8-8 8-14a8 8 0 0 0-8-8z" fill="none" stroke="#6d7896" stroke-width="1.5"/><circle cx="9" cy="9" r="3" fill="none" stroke="#6d7896" stroke-width="1.5"/></svg><div><b>Address:</b><br>48 Alder Lane, Boise, ID</div></div>
      <div class="info-row" style="margin-top:26px"><svg width="22" height="18" viewBox="0 0 22 18"><path d="M1 6c6-5 14-5 20 0l-3 3-3-2V5H7v2L4 9z" fill="none" stroke="#6d7896" stroke-width="1.5"/><rect x="5" y="10" width="12" height="7" fill="none" stroke="#6d7896" stroke-width="1.5"/></svg><div><b>Phone:</b><br>+1 555 014 2290</div></div>
      <div class="info-row" style="margin-top:26px"><svg width="18" height="24" viewBox="0 0 18 24"><rect x="3" y="1" width="12" height="22" rx="2" fill="none" stroke="#6d7896" stroke-width="1.5"/><path d="M7 19h4" stroke="#6d7896" stroke-width="1.5"/></svg><div><b>Mobile:</b><br>+1 555 014 2290</div></div>
      <div class="info-row" style="margin-top:26px"><svg width="22" height="16" viewBox="0 0 22 16"><rect x="1" y="1" width="20" height="14" fill="none" stroke="#6d7896" stroke-width="1.5"/><path d="M1 1l10 8 10-8" fill="none" stroke="#6d7896" stroke-width="1.5"/></svg><div><b>Email:</b><br>support@qrhvac.example</div></div>
    </div>
  </div>
  <div class="abs col" style="left:655px">
    <h5>QUICK LINKS</h5><div class="under"></div>
    <div class="links">
      <div>About<span>›</span></div><div>Contact<span>›</span></div><div>News List<span>›</span></div><div>Services<span>›</span></div><div style="border:0">Shop<span>›</span></div>
    </div>
  </div>
  <div class="abs col" style="left:969px">
    <h5>OPENING HOURS</h5><div class="under"></div>
    <div style="margin-top:14px">
      <div class="info-row"><svg width="26" height="26" viewBox="0 0 26 26"><circle cx="13" cy="13" r="12" fill="none" stroke="#6d7896" stroke-width="1.5"/><path d="M13 6v7h5" fill="none" stroke="#6d7896" stroke-width="1.5"/></svg><div><b>Monday - Friday</b><br>8:00 AM - 5:00 PM</div></div>
      <div class="info-row" style="margin-top:26px"><svg width="26" height="26" viewBox="0 0 26 26"><circle cx="13" cy="13" r="12" fill="none" stroke="#6d7896" stroke-width="1.5"/><path d="M13 6v7h5" fill="none" stroke="#6d7896" stroke-width="1.5"/></svg><div><b>Saturday</b><br>9:00 AM - 4:00 PM</div></div>
      <div class="info-row" style="margin-top:26px"><svg width="26" height="26" viewBox="0 0 26 26"><circle cx="13" cy="13" r="12" fill="none" stroke="#6d7896" stroke-width="1.5"/><path d="M13 6v7h5" fill="none" stroke="#6d7896" stroke-width="1.5"/></svg><div><b>Sunday</b><br>CLOSED</div></div>
    </div>
  </div>
</footer>

</body>
</html>
```